Cool Landing page with email address sign up (mockups provided)

I need a landing page for a service that will send a weekly email to people who are looking for jobs in startups. On the landing page there is a call to action (submit button) to register their email address. The service is called VentureRoster and it is a side project to try to assist startup companies with hiring people.

I just want one single form field "Email".

The feeling I want to give people is one of adventure. Imagine the person is living in Gdansk Poland, they are a technical/IT expert and have dreams of making it big in a Startup in London. This is his big chance, this is going to allow him to do it! He's signing up to a big promise! It should be cool, professional, exciting.

A major influence should be:
http://copperkettlefair.example/

There should also be a call to tweet in a cool way like on (http://www.behindfounders.example/).

Look at this - taking a leap of faith, like this:
http://pagebloomkit.example/wp-content/uploads/2011/09/19.jpg

This is super with the colours - striking!:
http://hueparlor.example/

Fly your kit higher!:
http://tobiasvrenn.example/

If necessary use sex to sell:
http://pagebloomkit.example/wp-content/uploads/2011/09/24.jpg

Some original art would work:
http://pagebloomkit.example/wp-content/uploads/2011/09/fx_ss_group1_sm_filtered_0000s_0007_Layer-14.jpg

This is effective for a call to action, I'm looking to you to act!:
http://pagebloomkit.example/wp-content/uploads/2011/09/weblance.jpg
Take inspiration from:
http://www.behindfounders.example/
http://ventureroster.example/
http://foundersdaily.example/

***N.B.: I would prefer original art background over a photo

Also:
http://pixeljournalhub.example/inspiration/a-showcase-of-landing-pages-designed-for-conversion
especially:
http://pixeljournalhub.example/wp-content/uploads/2011/09/01-landing.jpg
http://pixeljournalhub.example/wp-content/uploads/2011/09/04-landing.jpg
http://pixeljournalhub.example/wp-content/uploads/2011/10/texture21.jpg

I really like the colouring from Coder Bulletin:
http://news.quillforge.example/

Reason: I'm going to be away for a few days so I won't have enough time to properly provide feedback.

The payment is now guaranteed. This project is a single page only.

I've added a few more example landing pages that I like.

I've now added the ventureroster logo image that should be used.

I've updated brief with more examples of what I'm looking for

Reason: I'm still progressing with candidate designs.

Target Market(s)

Technical people, english not being their native language. Ambitious to work in London/Dublin in a tech startup company. They want to receive a weekly emails with startup jobs in london or dublin.

Requirements
Must have
• Eyes must be drawn to the email registration form to get them to submit their email address. The background image or website theme should encourage their desires to work in the big city in exciting startup companies.

Should have a prompt to tweet (once pressed I'll do my own popup)

```html
<!DOCTYPE html>
<html lang="en">
<head>
<meta charset="utf-8">
<title>Founders Daily — Amazing Jobs, Amazing People</title>
<link rel="stylesheet" href="https://fonts.googleapis.com/css2?family=Arimo:wght@700&display=swap">
<style>
  :root {
    --bar-black: #000000;
    --bar-text: #ffffff;
    --brand-cyan: #4fd0ff;
    --panel-bg: #f1f1f1;
    --ink: #000000;
    --muted: #ababab;
    --field-bg: #ffffff;
    --button-top: #8fe3ff;
    --button-bottom: #2fb8f5;
    --sky-top: #6f97b8;
    --sky-mid: #a9c3d8;
    --tower-dark: #1c2733;
  }
  * { box-sizing: border-box; margin: 0; padding: 0; }
  html, body { width: 1200px; height: 900px; overflow: hidden; }
  body {
    position: relative;
    font-family: "Arimo", Arial, sans-serif;
    font-weight: 700;
    background: var(--tower-dark);
  }
  .city-backdrop {
    position: absolute;
    inset: 0;
    background:
      radial-gradient(ellipse 520px 380px at 50% 25%, var(--sky-mid), transparent 70%),
      linear-gradient(90deg, var(--tower-dark) 0%, rgba(28,39,51,0.2) 22%, rgba(28,39,51,0) 45%, rgba(28,39,51,0.1) 70%, var(--tower-dark) 100%),
      linear-gradient(180deg, var(--sky-top) 0%, var(--sky-mid) 40%, #4b6378 75%, var(--tower-dark) 100%);
  }
  .top-bar {
    position: absolute;
    top: 0; left: 0;
    width: 1200px; height: 75px;
    background: var(--bar-black);
    box-shadow: 0 3px 8px rgba(0,0,0,0.5);
    color: var(--bar-text);
    font-size: 20px;
  }
  .follow-link {
    position: absolute;
    left: 120px; top: 22px;
    display: flex; align-items: center; gap: 10px;
    color: var(--bar-text); text-decoration: none;
  }
  .follow-mark {
    width: 32px; height: 32px;
    border-radius: 5px;
    background: var(--brand-cyan);
  }
  .main-nav {
    position: absolute;
    right: 40px; top: 26px;
    display: flex; gap: 38px;
  }
  .main-nav a { color: var(--bar-text); text-decoration: none; }
  .signup-panel {
    position: absolute;
    left: 248px; top: 190px;
    width: 706px; height: 561px;
    background: var(--panel-bg);
    border-radius: 6px;
    text-align: center;
  }
  .brand-title {
    position: absolute;
    left: 0; right: 0; top: 52px;
    font-size: 72px;
    line-height: 1;
    white-space: nowrap;
    color: var(--brand-cyan);
  }
  .tagline {
    position: absolute;
    left: 0; right: 0; top: 164px;
    font-size: 41px;
    line-height: 51px;
    color: var(--ink);
  }
  .audience-note {
    position: absolute;
    left: 83px; top: 293px;
    width: 584px;
    text-align: left;
    font-size: 19px;
    line-height: 25px;
    color: var(--brand-cyan);
  }
  .signup-form label {
    position: absolute;
    left: 87px; top: 390px;
    font-size: 41px;
    white-space: nowrap;
    color: var(--muted);
  }
  .email-field {
    position: absolute;
    left: 33px; top: 450px;
    width: 576px; height: 74px;
    border: 3px solid #dcdcdc;
    background: var(--field-bg);
    box-shadow: inset 0 2px 6px rgba(0,0,0,0.25);
    font: inherit; font-size: 28px; padding: 0 16px;
  }
  .go-button {
    position: absolute;
    left: 620px; top: 448px;
    width: 71px; height: 76px;
    border: 1px solid #d6eef8;
    border-radius: 6px;
    background: linear-gradient(180deg, var(--button-top), var(--button-bottom));
    box-shadow: 0 2px 4px rgba(0,0,0,0.25);
    color: #ffffff;
    font: inherit; font-size: 40px;
    cursor: pointer;
  }
</style>
</head>
<body>
  <div class="city-backdrop" role="img" aria-label="Upward view of glass office towers against a blue, cloudy sky"></div>

  <header class="top-bar">
    <a class="follow-link" href="#">Follow Us On Chirper <span class="follow-mark"></span></a>
    <nav class="main-nav">
      <a href="#">News</a>
      <a href="#">Directory</a>
      <a href="#">How It Works</a>
    </nav>
  </header>

  <main class="signup-panel">
    <h1 class="brand-title">FOUNDERS DAILY</h1>
    <p class="tagline">AMAZING JOBS , AMAZING<br>PEOPLE , AMAZING COMPANY</p>
    <p class="audience-note">Register if you’re a startup who needs the best candidates<br>or if you’re an amazing candidate who wants to work in the<br>best startup company</p>
    <form class="signup-form" action="#">
      <label for="email">Enter Your Email Address</label>
      <input class="email-field" id="email" type="email" name="email">
      <button class="go-button" type="submit">Go</button>
    </form>
  </main>
</body>
</html>
```